PlumVerse Business Cards

I need a business card designed for PlumVerse. To get an idea of what we do please visit https://brisklayout.example/para-artistas-7

```html
<!DOCTYPE html>
<html lang="en">
<head>
<meta charset="utf-8">
<title>PlumVerse Business Card</title>
<link rel="stylesheet" href="https://fonts.googleapis.com/css2?family=Figtree:wght@400;500;700&display=swap">
<style>
  :root {
    --stage: #505050;
    --ink: #222222;
    --paper: #ffffff;
    --amber: #e4931b;
    --text-light: #ffffff;
  }
  * { box-sizing: border-box; margin: 0; padding: 0; }
  html, body {
    width: 1133px; height: 1200px; overflow: hidden;
    background: var(--stage);
    font-family: "Figtree", "Helvetica Neue", Arial, sans-serif;
  }
  .card {
    position: absolute;
    left: 204px;
    width: 725px;
    height: 412px;
    overflow: hidden;
  }
  .card--front { top: 144px; background: var(--paper); }
  .card--back { top: 641px; background: var(--amber); }

  .front-shape { position: absolute; inset: 0; width: 725px; height: 412px; }
  .front-shape .stripe { fill: var(--amber); }
  .front-shape .gap { fill: var(--paper); }
  .front-shape .panel { fill: var(--ink); }

  .holder { position: absolute; left: 41px; top: 92px; color: var(--text-light); }
  .holder__name {
    font-size: 23px; font-weight: 700; color: var(--amber);
    letter-spacing: 0.01em; line-height: 1;
  }
  .holder__role { font-size: 16px; font-weight: 500; margin-top: 8px; }

  .contact { position: absolute; left: 41px; list-style: none; color: var(--text-light); }
  .contact--address { top: 157px; }
  .contact--lines { top: 214px; }
  .contact li {
    display: flex; align-items: flex-start;
    font-size: 16px; font-weight: 500; line-height: 20.5px;
  }
  .contact .icon {
    width: 14px; height: 14px; flex: none;
    margin: 3px 9px 0 0; fill: var(--amber);
  }

  .brand-name {
    position: absolute;
    font-weight: 400;
    letter-spacing: 0.2em;
    line-height: 1;
    white-space: nowrap;
  }
  .brand-name--front {
    left: 440px; width: 285px; text-align: center;
    top: 186px; font-size: 26px; color: var(--ink);
  }
  .brand-name--back {
    left: 0; width: 725px; text-align: center;
    top: 182px; font-size: 42px; color: var(--text-light);
  }
</style>
</head>
<body>

<section class="card card--front" aria-label="Card front">
  <svg class="front-shape" viewBox="0 0 725 412" aria-hidden="true">
    <polygon class="stripe" points="0,0 419,0 305,196 421,412 0,412"/>
    <polygon class="gap" points="0,0 411,0 298,196 413,412 0,412"/>
    <polygon class="panel" points="0,0 405,0 292,196 407,412 0,412"/>
  </svg>

  <div class="holder">
    <h1 class="holder__name">DANIEL HART</h1>
    <p class="holder__role">President</p>
  </div>

  <ul class="contact contact--address">
    <li>
      <svg class="icon" viewBox="0 0 14 14"><path d="M7 0.5a4.8 4.8 0 0 0-4.8 4.8C2.2 9 7 13.8 7 13.8s4.8-4.8 4.8-8.5A4.8 4.8 0 0 0 7 0.5zm0 6.8a2 2 0 1 1 0-4 2 2 0 0 1 0 4z"/></svg>
      <span>4120 Larkspur Court<br>Fairbanks, Alaska 99701</span>
    </li>
  </ul>

  <ul class="contact contact--lines">
    <li>
      <svg class="icon" viewBox="0 0 14 14"><path d="M3 0.8l2.2 2.8-1.3 1.6c0.8 1.8 2.3 3.3 4.1 4.1l1.6-1.3 2.8 2.2-1.4 2.4C5.6 12.4 1.6 8.4 0.8 3.1z"/></svg>
      <span>555-214-0187</span>
    </li>
    <li>
      <svg class="icon" viewBox="0 0 14 14"><path d="M3.5 0h7v14h-7zM4.8 1.6v9.6h4.4V1.6z"/></svg>
      <span>555-381-6402</span>
    </li>
    <li>
      <svg class="icon" viewBox="0 0 14 14"><path d="M3.5 0.5h7v4h-7zM0.5 5.5h13v6h-13zM3 10h8v3.5H3z"/></svg>
      <span>555-729-4453</span>
    </li>
    <li>
      <svg class="icon" viewBox="0 0 14 14"><path d="M0.5 3h13v8.5h-13zM1.5 3.8L7 8l5.5-4.2v-0.6H1.5z" fill-rule="evenodd"/></svg>
      <span>hart@plumverse.com</span>
    </li>
    <li>
      <svg class="icon" viewBox="0 0 14 14"><circle cx="7" cy="7" r="6.5"/><path d="M3 4.5l2.5 1 1 3-1.5 2-1.2-2.8zM8.5 2.5l2.5 1.5-0.5 2.5-2-1.5z" fill="#222"/></svg>
      <span>www.plumverse.com</span>
    </li>
  </ul>

  <p class="brand-name brand-name--front">PlumVerse</p>
</section>

<section class="card card--back" aria-label="Card back">
  <p class="brand-name brand-name--back">PlumVerse</p>
</section>

</body>
</html>
```